Bright Tutor Circle business card

Use existing logo to design a business card which contains information that is listed below. Use of logo as attached. It is important that the colour scheme matches the logo already designed. It needs to be crisp and professional. This is an on line business, a database of training providers for educational establishments. The website will provide users with full information on trainers who are available and their credibility.
Target Market(s)
Educators and training providers
Industry/Entity Type
Education
Contact Information for Business Card
See below for details
Font styles to use
Colors
Designer to choose colors to be used in the design.
Requirements
Must have
- Email address mara@brighttutorcircle.co.uk
- Twitter feed. @MaraBtc
- LinkedIn details Mara Fenwick
- Mobile phone number 07812 540913
- Mission statement: To create a learning network that ensures that schools receive first class training that is excellent value for money.
Nice to have
- N/a
Should not have
- Twee educational images

```html
<!DOCTYPE html>
<html lang="en">
<head>
<meta charset="utf-8">
<title>Bright Tutor Circle – Business Card</title>
<link rel="stylesheet" href="https://fonts.googleapis.com/css2?family=Questrial&display=swap">
<style>
  :root {
    --brand-blue: #1a8ad6;
    --brand-blue-deep: #0a72c2;
    --brand-blue-light: #2aa3e6;
    --ink: #1c1c1c;
    --paper: #ffffff;
    --backdrop: #eef0f2;
    --card-w: 520px;
    --card-h: 315px;
  }
  * { box-sizing: border-box; margin: 0; padding: 0; }
  html, body {
    width: 1200px;
    height: 800px;
    overflow: hidden;
    background: var(--backdrop);
    font-family: "Questrial", "Century Gothic", sans-serif;
  }
  .canvas {
    width: 1200px;
    height: 800px;
    display: flex;
    align-items: center;
    justify-content: center;
    gap: 60px;
  }
  .card {
    position: relative;
    width: var(--card-w);
    height: var(--card-h);
    overflow: hidden;
    box-shadow: 0 6px 18px rgba(0,0,0,0.12);
  }

  /* Back side */
  .card--back {
    background: linear-gradient(160deg, var(--brand-blue-light) 0%, var(--brand-blue) 45%, var(--brand-blue-deep) 100%);
    color: var(--paper);
  }
  .card__pattern {
    position: absolute;
    inset: 0;
    background: radial-gradient(ellipse at 75% 15%, rgba(255,255,255,0.14) 0%, rgba(255,255,255,0) 55%),
                radial-gradient(ellipse at 15% 85%, rgba(0,40,110,0.18) 0%, rgba(0,40,110,0) 60%);
  }
  .brand {
    position: absolute;
    display: flex;
    align-items: center;
    gap: 12px;
  }
  .brand__dot {
    width: 34px;
    height: 34px;
    border-radius: 50%;
    flex: none;
  }
  .brand__name {
    font-size: 30px;
    letter-spacing: 0.5px;
    white-space: nowrap;
    text-transform: uppercase;
  }
  .card--back .brand {
    top: 92px;
    left: 50%;
    transform: translateX(-50%);
  }
  .card--back .brand__dot { background: var(--paper); }
  .card--back .brand__name { color: var(--paper); }

  .mission {
    position: absolute;
    left: 36px;
    right: 36px;
    bottom: 48px;
    text-align: center;
    text-transform: uppercase;
    letter-spacing: 2px;
  }
  .mission__title {
    font-size: 12px;
    letter-spacing: 3px;
    margin-bottom: 8px;
  }
  .mission__text {
    font-size: 10px;
    line-height: 1.6;
  }

  /* Front side */
  .card--front { background: var(--paper); }
  .card--front .brand { top: 52px; left: 40px; }
  .card--front .brand__dot { background: var(--brand-blue); }
  .card--front .brand__name { color: var(--brand-blue); font-size: 26px; }

  .contact-list {
    position: absolute;
    left: 40px;
    top: 140px;
    list-style: none;
    color: var(--ink);
    font-size: 15px;
  }
  .contact-list__item {
    display: flex;
    align-items: center;
    gap: 8px;
    height: 21px;
  }
  .contact-list__icon {
    width: 14px;
    height: 14px;
    flex: none;
  }
  .contact-list__marker {
    width: 13px;
    height: 13px;
    border-radius: 50%;
    background: var(--brand-blue);
    flex: none;
    margin: 0 1px 0 0;
  }
  .wave {
    position: absolute;
    left: 0;
    bottom: 0;
    width: var(--card-w);
    height: var(--card-h);
  }
</style>
</head>
<body>
<main class="canvas">

  <section class="card card--back" aria-label="Business card, back">
    <div class="card__pattern" role="img" aria-label="Faint pattern of soft blue ovals across the card"></div>
    <div class="brand">
      <span class="brand__dot"></span>
      <span class="brand__name">Bright Tutor Circle</span>
    </div>
    <div class="mission">
      <h2 class="mission__title">Mission Statement</h2>
      <p class="mission__text">To create a learning network that ensures that schools receive first class training that is excellent value for money.</p>
    </div>
  </section>

  <section class="card card--front" aria-label="Business card, front">
    <div class="brand">
      <span class="brand__dot"></span>
      <span class="brand__name">Bright Tutor Circle</span>
    </div>

    <ul class="contact-list">
      <li class="contact-list__item">
        <svg class="contact-list__icon" viewBox="0 0 24 24" aria-hidden="true">
          <path fill="#1a8ad6" d="M6.6 10.8a15.1 15.1 0 0 0 6.6 6.6l2.2-2.2a1 1 0 0 1 1-.25 11.4 11.4 0 0 0 3.6.57 1 1 0 0 1 1 1V20a1 1 0 0 1-1 1A17 17 0 0 1 3 4a1 1 0 0 1 1-1h3.5a1 1 0 0 1 1 1c0 1.25.2 2.45.57 3.57a1 1 0 0 1-.25 1z"/>
        </svg>
        <span>07812 540913</span>
      </li>
      <li class="contact-list__item">
        <svg class="contact-list__icon" viewBox="0 0 24 24" aria-hidden="true">
          <rect x="2" y="5" width="20" height="14" rx="2" fill="#1a8ad6"/>
          <polyline points="3,6 12,13 21,6" fill="none" stroke="#ffffff" stroke-width="1.8"/>
        </svg>
        <span>mara@brighttutorcircle.co.uk</span>
      </li>
      <li class="contact-list__item">
        <span class="contact-list__marker"></span>
        <span>@MaraBtc</span>
      </li>
      <li class="contact-list__item">
        <span class="contact-list__marker"></span>
        <span>Mara Fenwick</span>
      </li>
    </ul>

    <svg class="wave" viewBox="0 0 520 315" aria-hidden="true">
      <defs>
        <linearGradient id="waveFill" x1="0" y1="0" x2="1" y2="1">
          <stop offset="0" stop-color="#2aa3e6"/>
          <stop offset="1" stop-color="#0a72c2"/>
        </linearGradient>
      </defs>
      <path d="M0,248 C110,222 210,300 330,276 C420,258 470,232 520,240 L520,315 L0,315 Z" fill="url(#waveFill)"/>
    </svg>
  </section>

</main>
</body>
</html>
```